Word template for proposals we send to clients

We want a word template designed based on the look/feel of our website. The website is www.brovanex.com.au and while we have pictures of 2 staff on the website we have pictures of other staff if required

the template will be used to send out proposals to potential clients, therefore it has to be professional, modern and compelling for someone to open

Target Market(s)

B2B

Industry/Entity Type

It Company

Font styles to use
Serif

Colors

Designer to choose colors to be used in the design.

Requirements
Must have
• Same look and feel as website
Nice to have
• Dont know what I am missing so anythign you feel i need to add

```html
<!DOCTYPE html>
<html lang="en">
<head>
<meta charset="utf-8">
<title>Brovanex Proposal Letterhead</title>
<link rel="stylesheet" href="https://fonts.googleapis.com/css2?family=Montserrat:wght@400;500;700&display=swap">
<style>
  :root {
    --slate-deep: #2b313b;
    --slate: #343a46;
    --slate-light: #566272;
    --lime: #b5c22b;
    --paper: #ffffff;
    --ink: #1d1d1d;
    --text-light: #ffffff;
  }
  * { margin: 0; padding: 0; box-sizing: border-box; }
  html, body { width: 930px; height: 1200px; overflow: hidden; background: var(--paper); }
  body { font-family: "Montserrat", Arial, sans-serif; }
  .letterhead { position: relative; width: 930px; height: 1200px; background: var(--paper); overflow: hidden; }
  .header-shapes { position: absolute; top: 0; left: 0; }

  .brand { position: absolute; left: 64px; top: 150px; display: flex; align-items: center; gap: 10px; }
  .brand-dot { width: 20px; height: 20px; border-radius: 50%; background: var(--lime); }
  .brand-name { font-weight: 700; font-size: 34px; color: var(--ink); letter-spacing: 0.5px; }

  .contact { position: absolute; color: var(--text-light); }
  .contact-row { display: flex; align-items: center; gap: 8px; white-space: nowrap; }
  .contact-row svg { flex: none; }
  .contact-online { left: 373px; top: 56px; font-size: 16px; }
  .contact-online .contact-row { height: 25.5px; }
  .contact-phone { left: 636px; top: 58px; font-size: 16px; line-height: 19px; }
  .contact-phone .contact-row { align-items: flex-start; }
  .contact-address { left: 636px; top: 105px; font-size: 10px; line-height: 12.5px; }
  .contact-address .contact-row { align-items: flex-start; }
  .phone-lines, .address-lines { display: flex; flex-direction: column; }

  .footer-band { position: absolute; left: 0; bottom: 0; width: 930px; height: 38px; background: var(--slate); }
  .footer-accent { position: absolute; left: 0; bottom: 0; width: 261px; height: 38px; background: var(--lime); }
</style>
</head>
<body>
<div class="letterhead">
  <svg class="header-shapes" width="930" height="175" viewBox="0 0 930 175" aria-hidden="true">
    <defs>
      <linearGradient id="panelShade" x1="0" x2="1" y1="0" y2="0">
        <stop offset="0" stop-color="#323844"/>
        <stop offset="0.6" stop-color="#576374"/>
        <stop offset="1" stop-color="#343a46"/>
      </linearGradient>
    </defs>
    <rect x="0" y="0" width="930" height="34" fill="var(--slate)"/>
    <polygon points="637,0 930,0 930,33 657,33" fill="var(--lime)"/>
    <rect x="0" y="34" width="930" height="138" fill="var(--slate-deep)"/>
    <polygon points="284,34 930,34 930,157 333,157" fill="url(#panelShade)"/>
    <polygon points="0,48 264,48 315,172 0,172" fill="var(--paper)"/>
    <rect x="0" y="172" width="930" height="3" fill="var(--paper)"/>
  </svg>

  <div class="brand">
    <span class="brand-dot"></span>
    <span class="brand-name">Brovanex</span>
  </div>

  <div class="contact contact-online">
    <div class="contact-row">
      <svg width="16" height="14" viewBox="0 0 16 14" fill="none" stroke="#fff" stroke-width="2"><path d="M2 11V8a6 6 0 0 1 12 0v3"/><rect x="1" y="9" width="2" height="4" fill="#fff" stroke="none"/><rect x="13" y="9" width="2" height="4" fill="#fff" stroke="none"/></svg>
      <span>support@brovanex.com.au</span>
    </div>
    <div class="contact-row">
      <svg width="16" height="14" viewBox="0 0 16 14" fill="none" stroke="#fff" stroke-width="1.4"><rect x="2" y="3" width="12" height="8"/><path d="M2 3l6 5 6-5M2 11l4.5-4M14 11L9.5 7"/></svg>
      <span>info@brovanex.com.au</span>
    </div>
    <div class="contact-row">
      <svg width="16" height="14" viewBox="0 0 16 14" fill="none" stroke="#fff" stroke-width="1.2"><circle cx="8" cy="7" r="5.5"/><ellipse cx="8" cy="7" rx="2.4" ry="5.5"/><path d="M2.5 7h11M3.5 4h9M3.5 10h9"/></svg>
      <span>https://www.brovanex.com.au/</span>
    </div>
  </div>

  <div class="contact contact-phone">
    <div class="contact-row">
      <svg width="14" height="14" viewBox="0 0 14 14" fill="none" stroke="#fff" stroke-width="1.5"><path d="M3 1.5l2 3-1.2 1.4a8 8 0 0 0 4.3 4.3L9.5 9l3 2-1.3 2A10 10 0 0 1 1 2.8z"/></svg>
      <div class="phone-lines">
        <span>1300 42 61 78</span>
        <span>+61 3 9047 5521</span>
      </div>
    </div>
  </div>

  <div class="contact contact-address">
    <div class="contact-row">
      <svg width="14" height="17" viewBox="0 0 14 17"><path d="M7 1a5.5 5.5 0 0 1 5.5 5.5C12.5 10 7 16 7 16S1.5 10 1.5 6.5A5.5 5.5 0 0 1 7 1z" fill="#fff"/><circle cx="7" cy="6.5" r="2" fill="var(--slate-light)"/></svg>
      <div class="address-lines">
        <span>Melbourne - Head Office Lvl 9/214 Harlow St</span>
        <span>Melbourne VIC 3000 Australia</span>
      </div>
    </div>
  </div>

  <div class="footer-band"></div>
  <div class="footer-accent"></div>
</div>
</body>
</html>
```